Poster to advertise new mind coaching clinic

Create a single sided A4 colour poster using the text provided. Suggested image provided. You may want to suggest an alternative however images need to appeal to both male and female sports people.

Text:
One-to-one mind coaching
For recreational and competitive sports people
Learn the mental tools and techniques used by the top sports people to fulfil your potential

 Create well-formed and achievable goals
 Overcome limiting beliefs
 Accelerate mastery through modelling your heroes
 Learn how to use mental rehearsal to increase your chances of success
 Smash through belief ceilings
 Get into the zone to bring your ‘A-Game’ more often
Thursdays in central Twyford
5-8pm
For more information contact:
stellvanementoring@quorvexmail.com
Tel: 07700 900482
www.stellvane-mind.co.uk

sports people

Clinic

• All the content provided. Contact details.

```html
<!DOCTYPE html>
<html lang="en">
<head>
<meta charset="utf-8">
<title>One-to-One Mind Coaching – Stellvane</title>
<link rel="stylesheet" href="https://fonts.googleapis.com/css2?family=Bebas+Neue&family=Teko:wght@400;500&display=swap">
<style>
  :root {
    --sky-deep: #1f5fa8;
    --sky-mid: #2fa6c9;
    --mint: #a8f2e8;
    --mint-soft: #c8f7ef;
    --meadow: #7fb98f;
    --hill: #6f9f78;
    --water: #5fcfc6;
    --water-light: #9be8e0;
    --navy: #17323f;
    --ink: #1b2a33;
    --white: #ffffff;
    --title-yellow: #f2f23a;
    --title-navy: #1a4254;
    --footer-band: rgba(20, 34, 40, 0.9);
    --footer-text: #6fe6ee;
  }
  * { margin: 0; padding: 0; box-sizing: border-box; }
  html, body { width: 848px; height: 1200px; overflow: hidden; background: var(--white); }
  .poster {
    position: relative;
    width: 848px;
    height: 1200px;
    overflow: hidden;
    font-family: "Bebas Neue", "Arial Narrow", sans-serif;
  }
  .sky {
    position: absolute; inset: 0;
    background:
      radial-gradient(ellipse 65% 30% at 22% 14%, rgba(31,95,168,0.9), transparent 70%),
      radial-gradient(ellipse 55% 30% at 80% 34%, rgba(220,252,246,0.95), transparent 70%),
      linear-gradient(180deg, var(--sky-mid) 0%, #6fd2d6 22%, var(--mint) 42%, var(--mint-soft) 52%, var(--mint) 62%);
  }
  .scene-photo {
    position: absolute;
    left: 0; top: 560px;
    width: 848px; height: 560px;
    background:
      radial-gradient(ellipse 60% 30% at 50% 92%, rgba(190,245,238,0.75), transparent 70%),
      linear-gradient(180deg, rgba(168,242,232,0) 0%, var(--mint) 14%, #a9dcc6 30%, var(--meadow) 46%, var(--hill) 58%, #74b59e 70%, var(--water) 84%, var(--water-light) 100%);
  }
  .title {
    position: absolute; left: 16px; top: 18px; width: 816px;
    font-size: 92px; line-height: 1; letter-spacing: 1px; white-space: nowrap; font-weight: 400;
    background: linear-gradient(90deg, var(--title-yellow) 0%, var(--title-yellow) 45%, #8b9a3a 55%, var(--title-navy) 68%, var(--title-navy) 100%);
    -webkit-background-clip: text; background-clip: text; color: transparent;
  }
  .subtitle {
    position: absolute; left: 64px; top: 106px;
    font-size: 46px; line-height: 1; color: var(--navy); letter-spacing: 2.5px; white-space: nowrap;
  }
  .tagline {
    position: absolute; left: 43px; top: 172px;
    font-size: 40px; line-height: 48px; color: var(--white); letter-spacing: 2.4px; white-space: nowrap;
    text-shadow: 0 1px 3px rgba(0,0,0,0.35);
  }
  .benefits {
    position: absolute; left: 58px; top: 292px;
    list-style: none; color: var(--ink);
    font-size: 25px; line-height: 29.4px; letter-spacing: 1.5px; white-space: nowrap;
  }
  .benefits li { position: relative; padding-left: 24px; }
  .benefits li::before {
    content: ""; position: absolute; left: 2px; top: 9px;
    width: 9px; height: 9px; border-radius: 50%; background: var(--ink);
  }
  .schedule {
    position: absolute; left: 58px; top: 492px;
    font-size: 30px; line-height: 35px; color: var(--white); letter-spacing: 1.2px;
    text-shadow: 0 1px 3px rgba(0,0,0,0.35);
  }
  .brand {
    position: absolute; left: 42px; top: 690px;
    display: flex; align-items: center; gap: 12px;
    font-size: 54px; line-height: 1; color: var(--ink);
  }
  .brand-dot { width: 30px; height: 30px; border-radius: 50%; background: var(--ink); }
  .contact-band {
    position: absolute; left: 0; bottom: 0; width: 848px; height: 80px;
    background: var(--footer-band);
    font-family: "Teko", "Arial Narrow", sans-serif; font-weight: 500;
    color: var(--footer-text); font-size: 27px; line-height: 30px;
  }
  .contact-left { position: absolute; left: 46px; top: 11px; }
  .contact-right { position: absolute; right: 44px; top: 11px; text-align: right; }
</style>
</head>
<body>
<main class="poster">
  <div class="sky" role="img" aria-label="Bright teal and blue sky background"></div>
  <div class="scene-photo" role="img" aria-label="Photo of a celebrating sprinter in team kit holding a relay baton, rising from splashing water in front of green mountain peaks"></div>

  <h1 class="title">ONE-TO-ONE MIND COACHING</h1>
  <p class="subtitle">FOR RECREATIONAL AND COMPETITIVE SPORTS</p>
  <p class="tagline">LEARN THE MENTAL TOOLS AND TECHNIQUES USED BY<br>THE TOP SPORTS PEOPLE TO FULFIL YOUR POTENTIAL</p>

  <ul class="benefits">
    <li>CREATE WELL-FORMED AND ACHIEVABLE GOALS</li>
    <li>OVERCOME LIMITING BELIEFS</li>
    <li>ACCELERATE MASTERY THROUGH MODELLING YOUR HEROES</li>
    <li>LEARN HOW TO USE MENTAL REHEARSAL TO INCREASE YOUR CHANCES OF SUCCESS</li>
    <li>SMASH THROUGH BELIEF CEILINGS</li>
    <li>GET INTO THE ZONE TO BRING YOUR ‘A-GAME’ MORE OFTEN</li>
  </ul>

  <p class="schedule">THURSDAYS IN CENTRAL TWYFORD<br>5-8PM</p>

  <div class="brand"><span class="brand-dot"></span><span class="brand-name">STELLVANE</span></div>

  <footer class="contact-band">
    <div class="contact-left">For more information contact:<br>stellvanementoring@quorvexmail.com</div>
    <div class="contact-right">Tel: 07700 900482<br>www.stellvane-mind.co.uk</div>
  </footer>
</main>
</body>
</html>
```